Business Card Design Project

Hello Designers, hope you are all aiming enjoy the weekend
I have the Business Logo (uploaded), you can alter the color which ever way you think would work,
Im looking for a simple yet striking feel, something which will stay memorable (I have uploaded 3 examples for you to flick through)
Information on the card, will just be the bare minimum,
Double Sided
Info being
i.e.
Name
Number
Website
ABN
Tobin Wexmoor
+468213579 (singapore)
+315792846 (Australia)
+729384615 (America)
www.lomevu-linkup.example
ABN 86420913
Enjoy,
Tobin
Industry/Entity Type
Business
Look and feel
Each slider illustrates characteristics of the customer's brand and the style your logo design should communicate.

```html
<!DOCTYPE html>
<html lang="en">
<head>
<meta charset="utf-8">
<title>Lomevu Linkup — Business Card</title>
<link href="https://fonts.googleapis.com/css2?family=Questrial&display=swap" rel="stylesheet">
<style>
  :root {
    --page-bg: #ffffff;
    --card-stock: #e4e2cb;
    --teal: #1e7f7a;
    --ink: #2a2a28;
    --ink-soft: #4a4a45;
    --shadow: rgba(0, 0, 0, 0.28);
  }
  * { margin: 0; padding: 0; box-sizing: border-box; }
  html, body {
    width: 1200px;
    height: 1200px;
    overflow: hidden;
    background: var(--page-bg);
    font-family: "Questrial", "Century Gothic", sans-serif;
  }
  .sheet {
    width: 1200px;
    height: 1200px;
    display: flex;
    flex-direction: column;
    align-items: center;
    justify-content: center;
    gap: 70px;
  }
  .card {
    width: 760px;
    height: 362px;
    border-radius: 14px;
    box-shadow: 2px 4px 8px var(--shadow);
    overflow: hidden;
  }
  .card-front {
    background: var(--card-stock);
    display: flex;
    flex-direction: column;
    align-items: center;
    justify-content: center;
    text-align: center;
  }
  .brand {
    display: flex;
    align-items: center;
    gap: 14px;
    color: var(--ink);
    font-size: 50px;
    letter-spacing: 0.5px;
    line-height: 1;
  }
  .brand-mark {
    width: 34px;
    height: 34px;
    background: var(--teal);
  }
  .holder-name {
    margin-top: 24px;
    color: var(--teal);
    font-size: 26px;
    letter-spacing: 5px;
    text-transform: uppercase;
  }
  .contact {
    margin-top: 22px;
    color: var(--ink-soft);
    font-size: 17px;
    letter-spacing: 2px;
    line-height: 1.75;
    text-transform: uppercase;
  }
  .card-back {
    background: var(--teal);
  }
  .card-back svg { display: block; width: 100%; height: 100%; }
</style>
</head>
<body>
  <main class="sheet">
    <section class="card card-front">
      <div class="brand">
        <span>Lomevu</span>
        <span class="brand-mark" aria-hidden="true"></span>
        <span>Linkup</span>
      </div>
      <p class="holder-name">Tobin Wexmoor</p>
      <div class="contact">
        <p>+468213579 (Singapore) +315792846 (Australia)</p>
        <p>+729384615 (America) www.lomevu-linkup.example</p>
        <p>ABN 86420913</p>
      </div>
    </section>
    <section class="card card-back" role="img" aria-label="Repeating brand pattern in teal and cream covering the reverse of the card">
      <svg viewBox="0 0 760 362" preserveAspectRatio="none" aria-hidden="true">
        <defs>
          <linearGradient id="back-tone" x1="0" y1="0" x2="1" y2="1">
            <stop offset="0" stop-color="#2a8a84"/>
            <stop offset="1" stop-color="#1c7670"/>
          </linearGradient>
        </defs>
        <rect width="760" height="362" fill="url(#back-tone)"/>
      </svg>
    </section>
  </main>
</body>
</html>
```